Kelvaro, The smart answer for charity drives

Kelvaro needs a simple Wordpress website development. The key message is that we have three wins in fundraising according to my services - win for theorganisation - win for the partner and win for the audience and the community.STYLE:- My business card is attached so the site colors could match with the card;- We love the style of this website: https://www.marenboltwick.co.nz/ because it is modern, minimalist, clean and easy to navigate. I am happy to have a similar parallax (scrolling) site as the reference samplePlease feature the following on the site:* INTRODUCTION (or About)* SERVICES* MY QUOTE* CONTACT US* PLAXTERN ( the contents are in the attached .rtf file - please message me if you are unable to open this document)Deliverables:- I would like a fully functioning (Coded) wordpress site

• Personable approach
• It is all about You (the other person who is approach my business)

```html
<!DOCTYPE html>
<html lang="en">
<head>
<meta charset="utf-8">
<title>Kelvaro – Nadia Korvellis-Brand</title>
<link href="https://fonts.googleapis.com/css2?family=Open+Sans:wght@300;400&family=Questrial&family=Ubuntu:wght@400;500&display=swap" rel="stylesheet">
<style>
:root{
  --ink:#1d1a1a;
  --body:#2b2727;
  --muted:#6a6464;
  --rule:#d9d4d1;
  --sand:#efe0d3;
  --rose:#c4968c;
  --button:#221d1d;
  --white:#ffffff;
  --field:#cfcaca;
}
*{margin:0;padding:0;box-sizing:border-box}
html,body{width:1200px;height:2445px;overflow:hidden}
body{font-family:"Questrial",sans-serif;color:var(--body);background:var(--white);position:relative}
.hero{position:absolute;left:0;top:0;width:1200px;height:448px;
  background:linear-gradient(90deg,#7a4b3c 0%,#8f5e4c 30%,#6e4a3c 55%,#3d2f28 72%,#c9a993 86%,#d9b9a0 100%)}
.hero-photo{position:absolute;inset:0}
.hero-shade{position:absolute;inset:0;background:rgba(40,22,18,.25)}
.brand{position:absolute;left:179px;top:34px;font-size:25px;color:var(--white);letter-spacing:.5px}
.nav{position:absolute;left:648px;top:44px;display:flex;gap:22px;list-style:none}
.nav li{font-size:14px;color:var(--white);letter-spacing:.3px}
.identity{position:absolute;left:306px;top:140px;width:492px;text-align:center;color:var(--white)}
.identity .rule{height:1px;background:rgba(255,255,255,.75)}
.identity h1{font-family:"Open Sans",sans-serif;font-weight:300;font-size:34px;line-height:48px;white-space:nowrap}
.credentials{font-family:"Open Sans",sans-serif;font-weight:300;font-size:15.5px;letter-spacing:1px;margin-top:9px}
.contact-card{position:absolute;left:306px;top:266px;color:var(--white);font-size:13px}
.contact-card dl{display:grid;grid-template-columns:71px 1fr;row-gap:14px;line-height:18px}
.contact-card dt{font-weight:600}
.contact-card a{color:var(--white);text-decoration:underline}
.section-title{font-family:"Ubuntu",sans-serif;font-weight:500;font-size:26px;color:var(--ink)}
.about{position:absolute;left:179px;top:556px;width:852px}
.intro{margin-top:26px;font-size:13.5px;font-weight:600;line-height:21px;color:var(--ink)}
.quote{margin-top:48px;border-top:2px solid var(--rule);border-bottom:2px solid var(--rule);height:98px;display:flex;align-items:center;font-size:14.6px;color:var(--muted);letter-spacing:.1px;white-space:nowrap;width:852px}
.bio{margin-top:48px}
.bio p{font-size:12.1px;line-height:16.5px;margin-bottom:22px}
.services{position:absolute;left:0;top:1467px;width:1200px;height:378px;background:var(--sand)}
.services .section-title{position:absolute;left:179px;top:56px}
.service-list{position:absolute;top:151px;list-style:none;font-size:12.3px;line-height:22.4px;color:var(--ink)}
.service-list li::before{content:"";display:inline-block;width:5px;height:5px;border-radius:50%;background:var(--ink);margin-right:10px;vertical-align:middle}
.col-a{left:179px}.col-b{left:472px}
.contact{position:absolute;left:179px;top:1900px;width:852px}
.field{border:1px solid var(--field);height:39px;margin-top:10px;padding:12px 20px;font-size:11px;color:#8a8585}
.field:first-of-type{margin-top:33px}
.field.message{height:182px}
.submit{margin-top:14px;height:41px;background:var(--button);color:var(--white);text-align:center;line-height:41px;font-family:"Ubuntu",sans-serif;font-size:15px;letter-spacing:1px}
.footer{position:absolute;left:0;top:2383px;width:1200px;height:62px;background:var(--rose);color:var(--white);font-size:11.5px}
.footer .copy{position:absolute;left:179px;top:23px}
.footer .social{position:absolute;right:165px;top:14px;display:flex;align-items:center;gap:8px;font-size:11px;letter-spacing:.5px}
.footer .social .box{width:33px;height:33px;border:1px solid var(--white)}
</style>
</head>
<body>
<header class="hero">
  <div class="hero-photo" role="img" aria-label="Portrait photograph of Nadia Korvellis-Brand against a warm blurred interior"></div>
  <div class="hero-shade"></div>
  <div class="brand">Kelvaro</div>
  <ul class="nav"><li>HOME</li><li>ABOUT</li><li>SERVICES</li><li>CONTACT US</li></ul>
  <div class="identity">
    <div class="rule"></div>
    <h1>Nadia Korvellis-Brand</h1>
    <div class="rule"></div>
    <p class="credentials">MDIPL &nbsp;|&nbsp; BINTST &nbsp;|&nbsp; B.SC</p>
  </div>
  <div class="contact-card">
    <dl>
      <dt>Address :</dt><dd>Kelvaro<br>412 Harbour Lane, Westmere, 0914, Auckland</dd>
      <dt>Phone :</dt><dd><a>021 73 19 52</a></dd>
      <dt>Email :</dt><dd><a>nadia@kelvaro.co.nz</a></dd>
    </dl>
  </div>
</header>

<section class="about">
  <h2 class="section-title">About Nadia Korvellis-Brand</h2>
  <p class="intro">I come from Greece where I completed my Bachelor in Political Science and International Studies. I continued my studies in UK, in Birmingham where I received a Master's Degree in Diplomacy.</p>
  <blockquote class="quote">'I look forward to working with you and your team and together achieving results that will make a difference where we live'</blockquote>
  <div class="bio">
    <p>Further education includes Mara Tollefsen-Ruiz courses, Board Leaders Institute governance courses, Riverbend University Contract's Law and a 2017 Eastbrook University paper on 'Disruptive Strategy'.</p>
    <p>I worked at the 2004 Summer Games Organising Committee in 2001 looking after the National Adaptive Sport Committees as the Deputy Manager in the International Relations Department.</p>
    <p>I moved to New Zealand in 2004 at the end of the games. I worked at Harbourside City Council as the sponsorship manager of festivals and community events, moved to Riverton where I worked at Netball Midlands, became the executive officer for Swim Midlands for 2 years, held contracts with my own sponsorship and marketing business (Kelvaro) with Gut Health Trust, Netball Midlands Coast, Civic Leisure, Homes for Families, various Councils and other organizations. Four years ago, I worked for Riverton City Council as the Partnership Manager for Major Projects, exceeding a target of $7.2m for Riverton Gardens Development Project over an eighteen-month period, $1m for River Plan and $750,000 for the Playgrounds of the Future Programme.</p>
    <p>My most recent job before re-establishing my own business was the Director of Philanthropy for Harbourside Heritage Museum where I was responsible for 'giving and legacy' programmes and developed an innovative bequest programme 'Your Lasting Gift'.</p>
    <p>I hold New Zealand Citizenship.</p>
    <p>I am passionate about my family, the adaptive sport movement, enjoy music, cooking Greek food and travelling.</p>
    <p>I have had governance experience with Open Hands, Parasport Midlands, Hillcrest Valley School Board of Trustees and as President of the Hellenic Society of Harbourside for 5 years.</p>
    <p>I am a current a member of Board Leaders Institute and Women in Governance.</p>
    <p>My greatest passion is people. I am grateful to all the teams that I worked with and the results that we achieved together. I always meet with potential partners to identify their objectives and outcomes, then tailor proposals to fit both their desires, the project's objectives and communities' interests. My approach is tailored and very personal. I believe this is the point of difference. I have developed strong relationships with funders, commercial businesses and donors during the years due to this approach.</p>
    <p>I am excited with projects that have an impact in the community and in our country.</p>
  </div>
</section>

<section class="services">
  <h2 class="section-title">Services</h2>
  <ul class="service-list col-a">
    <li>Fundraising Strategic Action Plans</li><li>Marketing Plans</li><li>Workshops on fundraising</li><li>Evaluation on fundraising projects</li><li>Funding applications</li><li>Commercial partnerships</li>
  </ul>
  <ul class="service-list col-b">
    <li>Giving Programmes</li><li>Legacy Programmes</li><li>Capital Projects Fundraising</li><li>Feasibility Studies</li><li>Consultancy on fundraising</li><li>Mentoring on fundraising</li>
  </ul>
</section>

<section class="contact">
  <h2 class="section-title">Contact Us</h2>
  <div class="field">Name..</div>
  <div class="field">Email..</div>
  <div class="field message">Message..</div>
  <div class="submit">SUBMIT</div>
</section>

<footer class="footer">
  <span class="copy">©Copyright information here</span>
  <span class="social"><span>PLAXTERN</span><span class="box"></span></span>
</footer>
</body>
</html>
```